Vemtra Group: Business Card for a high end technology company

We need a cool new design for our business cards using our cloud logo. We are a technology consulting business. We pride ourselves on be the best of the best. We mainly focus on cloud solutions and managed services. We need a business card that sets us apart from the other technology companies in the area and allows us to stand out.

Target Market(s)

Technology departments, CIO, CEOs, and Information Technology Staff.

Industry/Entity Type

Information Technology

Contact Information for Business Card

Must have the logo and our name.
Must have employee name, email address, office phone, cell phone and website.
Need to have all info on one side a cool design on backside.

Font styles to use
Serif
Sans Serif

Requirements
Must have
• Must have the logo and our name.
• Must have employee name, email address, office phone, cell phone and website.
• Need to have all info on one side a cool design on back side.
• Must be a crisp clean design, not too busy or confusing.

```html
<!DOCTYPE html>
<html lang="en">
<head>
<meta charset="utf-8">
<title>Vemtra Group – Business Card</title>
<link rel="stylesheet" href="https://fonts.googleapis.com/css2?family=Montserrat:wght@400;600;700&display=swap">
<style>
  :root {
    --page-bg: #2a2a2c;
    --card-white: #f4f5f6;
    --card-grey: #dcdfe2;
    --blue-deep: #1a6fb5;
    --blue-mid: #2f8fd6;
    --blue-light: #4fb8ea;
    --ink: #2b2b2e;
    --ink-soft: #4a4b50;
    --icon-blue: #2f8fd6;
  }
  * { margin: 0; padding: 0; box-sizing: border-box; }
  html, body { width: 1200px; height: 900px; overflow: hidden; }
  body {
    background: var(--page-bg);
    font-family: "Montserrat", Arial, sans-serif;
    position: relative;
  }
  .card {
    position: absolute;
    left: 270px;
    width: 660px;
    height: 377px;
    border-radius: 22px;
    overflow: hidden;
  }
  .card--back { top: 50px; }
  .card--front { top: 473px; background: linear-gradient(160deg, #ffffff 0%, var(--card-white) 55%, var(--card-grey) 100%); }

  .back-artwork {
    position: absolute;
    inset: 0;
    background: linear-gradient(150deg, var(--blue-light) 0%, var(--blue-mid) 50%, var(--blue-deep) 100%);
  }

  .back-brand {
    position: absolute;
    right: 70px;
    top: 120px;
    text-align: right;
    color: var(--ink);
  }
  .back-brand .brand-name { font-size: 42px; font-weight: 400; letter-spacing: 0.5px; }
  .back-brand .brand-web { font-size: 13px; font-weight: 700; margin-top: 2px; }

  .front-band { position: absolute; inset: 0; width: 100%; height: 100%; }

  .front-brand {
    position: absolute;
    left: 52px;
    top: 70px;
    display: flex;
    align-items: center;
    gap: 12px;
  }
  .front-brand .brand-dot {
    width: 34px; height: 34px; border-radius: 50%;
    background: var(--blue-mid);
  }
  .front-brand .brand-name { font-size: 30px; font-weight: 400; color: var(--ink); }

  .front-web {
    position: absolute;
    left: 52px;
    top: 262px;
    font-size: 14px;
    font-weight: 700;
    color: var(--ink);
    letter-spacing: 0.5px;
  }

  .contact {
    position: absolute;
    left: 370px;
    top: 62px;
    color: var(--ink);
  }
  .contact .person-name { font-size: 18px; font-weight: 700; letter-spacing: 0.5px; }
  .contact .person-title { font-size: 13px; font-weight: 400; color: var(--ink-soft); letter-spacing: 1px; margin-top: 2px; }
  .contact ul { list-style: none; margin-top: 14px; }
  .contact li { display: flex; align-items: center; gap: 8px; font-size: 17px; margin-bottom: 6px; color: var(--ink-soft); }
  .contact li svg { width: 16px; height: 16px; flex: none; }
</style>
</head>
<body>

  <section class="card card--back" aria-label="Card back">
    <div class="back-artwork" role="img" aria-label="Abstract blue wave artwork across the card back"></div>
    <div class="back-brand">
      <div class="brand-name">Vemtra Group</div>
      <div class="brand-web">www.vemtragroup.com</div>
    </div>
  </section>

  <section class="card card--front" aria-label="Card front">
    <svg class="front-band" viewBox="0 0 660 377" preserveAspectRatio="none" aria-hidden="true">
      <defs>
        <linearGradient id="band" x1="0" y1="0" x2="1" y2="0">
          <stop offset="0" stop-color="#1a6fb5"/>
          <stop offset="1" stop-color="#2f8fd6"/>
        </linearGradient>
      </defs>
      <path d="M0 330 C250 300 470 255 660 215 L660 377 L0 377 Z" fill="url(#band)"/>
      <path d="M0 330 C250 300 470 255 660 215 L660 232 C470 270 260 312 0 345 Z" fill="#4fb8ea" opacity="0.7"/>
    </svg>

    <div class="front-brand">
      <span class="brand-dot"></span>
      <span class="brand-name">Vemtra Group</span>
    </div>

    <div class="front-web">www.vemtragroup.com</div>

    <div class="contact">
      <div class="person-name">DANIEL HARTWELL</div>
      <div class="person-title">MANAGING DIRECTOR</div>
      <ul>
        <li>
          <svg viewBox="0 0 16 16"><path d="M2 7 C2 3 14 3 14 7 L11 8 L10 6 L6 6 L5 8 Z" fill="var(--icon-blue)"/><rect x="4" y="8.5" width="8" height="5" rx="1.5" fill="var(--icon-blue)"/></svg>
          5550 142 377
        </li>
        <li>
          <svg viewBox="0 0 16 16"><rect x="4" y="1" width="8" height="14" rx="2" fill="none" stroke="var(--icon-blue)" stroke-width="1.6"/><circle cx="8" cy="12" r="1" fill="var(--icon-blue)"/></svg>
          8880 316 204
        </li>
        <li>
          <svg viewBox="0 0 16 16"><rect x="1" y="3" width="14" height="10" rx="1" fill="var(--icon-blue)"/><path d="M1.5 3.5 L8 9 L14.5 3.5" fill="none" stroke="#fff" stroke-width="1.2"/></svg>
          dhartwell@vemtragroup.com
        </li>
      </ul>
    </div>
  </section>

</body>
</html>
```